Packaging design for a reclosable bag for our product

We have a logo, and we need to put it on packaging for our product and while we want the look to be simple, we want it to follow good design principles and also contain spaces for other product descriptions.

There will be 5 sizes at launch so I'd like 5 variations, one for each size.

I've included a few mockups of the type of bag that I made but they are all just rough ideas that I had.

I want the brand to look scientific and methodical and even a bit quirky, as in "wow this is a serious product but also a bit unusual."

```html
<!DOCTYPE html>
<html lang="en">
<head>
<meta charset="utf-8">
<title>Kelvo Bias Lighting – Bag</title>
<link rel="stylesheet" href="https://fonts.googleapis.com/css2?family=Montserrat:wght@500;700&display=swap">
<style>
  :root {
    --backdrop: #e6e6e6;
    --bag: #0d0d0d;
    --ink: #f2f2f2;
  }
  * { margin: 0; padding: 0; box-sizing: border-box; }
  html, body {
    width: 1200px;
    height: 960px;
    overflow: hidden;
    background: var(--backdrop);
    font-family: "Montserrat", sans-serif;
  }
  .bag {
    position: absolute;
    left: 290px;
    top: 70px;
    width: 620px;
    height: 820px;
    background: var(--bag);
    color: var(--ink);
  }
  .bag__handle {
    position: absolute;
    left: 250px;
    top: 56px;
    width: 150px;
    height: 44px;
    border-radius: 22px;
    background: var(--backdrop);
  }
  .brand-name {
    position: absolute;
    left: 60px;
    right: 60px;
    top: 270px;
    font-weight: 700;
    font-size: 128px;
    line-height: 1;
    letter-spacing: 2px;
    text-align: right;
  }
  .product {
    position: absolute;
    right: 64px;
    top: 440px;
    text-align: right;
  }
  .product__title {
    font-weight: 700;
    font-size: 48px;
    letter-spacing: 1px;
    line-height: 1.1;
    margin-bottom: 34px;
  }
  .product__size,
  .product__spec {
    font-weight: 500;
    font-size: 26px;
    line-height: 1.25;
    letter-spacing: 1px;
  }
  .product__size { margin-bottom: 16px; }
</style>
</head>
<body>
  <div class="bag">
    <div class="bag__handle"></div>
    <div class="brand-name">KELVO</div>
    <div class="product">
      <h1 class="product__title">BIAS LIGHTING</h1>
      <p class="product__size">EXTRA LARGE<br>5 METERS</p>
      <p class="product__spec">SIMULATED D65 CRI 90+<br>6500K WHITE BIAS LIGHTING</p>
    </div>
  </div>
</body>
</html>
```